Bref créative
Varneth Systems Stationery
Business card, envelops and letterhead
Bright & Fun-filled
Dorian Kelbrook
President & Chief Architect
418 W. Harrow Ln.
Kent, WA 98047
dorian.kelbrook@varneth.example
http://www.varneth.example
Please provide duplicate ai files in Illustrator 8.0 format and simlilar lower versions of any other files you provide as well as the originals
Logo only (without name)
Tag line:
"Providing Enterprise Business Solutions"
Original AI files

```html
<!DOCTYPE html>
<html lang="en">
<head>
<meta charset="utf-8">
<title>Varneth Systems Stationery</title>
<link href="https://fonts.googleapis.com/css2?family=Montserrat:wght@700;800&family=Open+Sans:wght@400;600&display=swap" rel="stylesheet">
<style>
  :root {
    --navy: #27378a;
    --navy-deep: #1d2a6e;
    --grey: #a3a5ab;
    --grey-light: #e4e5e8;
    --paper: #ffffff;
    --ink: #4a4c55;
    --backdrop: #ece9e4;
  }
  * { margin: 0; padding: 0; box-sizing: border-box; }
  html, body { width: 1200px; height: 506px; overflow: hidden; background: var(--backdrop); font-family: "Open Sans", Arial, sans-serif; color: var(--ink); }
  .canvas { position: relative; width: 1200px; height: 506px; }

  .sheet { position: absolute; background: var(--paper); box-shadow: 0 2px 6px rgba(0,0,0,.18); overflow: hidden; }
  .wave { position: absolute; left: 0; bottom: 0; width: 100%; }

  .brand { position: absolute; display: flex; align-items: center; gap: 4px; }
  .brand-dot { width: 12px; height: 12px; border-radius: 50%; background: var(--navy); }
  .brand-name { font-family: "Montserrat", Arial, sans-serif; font-weight: 800; color: var(--navy); font-size: 10px; letter-spacing: .3px; text-transform: uppercase; }

  .contact { position: absolute; font-size: 4.2px; line-height: 6px; color: var(--ink); }
  .web { position: absolute; font-size: 5px; color: #fff; font-weight: 600; }

  .faint-mark { position: absolute; border-radius: 50%; background: var(--grey-light); opacity: .55; }

  .option-label { position: absolute; top: 488px; font-size: 6px; color: #555; }

  .fax-title { position: absolute; left: 26px; top: 128px; font-family: "Montserrat", Arial, sans-serif; font-weight: 700; font-size: 17px; color: var(--navy-deep); }
  .fax-fields { position: absolute; left: 26px; top: 156px; width: 290px; display: grid; grid-template-columns: 1fr 1fr; column-gap: 20px; row-gap: 9px; font-size: 5px; }
  .fax-field { border-bottom: 0.6px solid #888; padding-bottom: 1px; }
  .fax-checks { position: absolute; left: 26px; top: 224px; width: 290px; display: flex; justify-content: space-between; font-size: 4.5px; }
  .fax-check { display: flex; align-items: center; gap: 2px; }
  .fax-check::before { content: ""; width: 5px; height: 5px; border: 0.6px solid #777; }

  .envelope { position: absolute; background: var(--paper); box-shadow: 0 2px 6px rgba(0,0,0,.2); overflow: hidden; }
  .flap { position: absolute; left: 0; top: 0; width: 100%; height: 100%; }
  .flap-mark { position: absolute; left: 50%; top: 16px; width: 34px; height: 34px; margin-left: -17px; border-radius: 50%; border: 3px solid #fff; }

  .card { position: absolute; width: 156px; height: 84px; border-radius: 6px; overflow: hidden; box-shadow: 0 2px 5px rgba(0,0,0,.2); }
  .card-front { background: var(--paper); }
  .card-back { background: linear-gradient(135deg, #c8c9cc, #a9abb0); }
  .card-person { position: absolute; left: 10px; top: 38px; font-size: 4.5px; line-height: 6px; }
  .card-person strong { font-weight: 600; color: var(--navy); }
  .card-back-mark { position: absolute; left: 24px; top: 20px; width: 44px; height: 44px; border-radius: 50%; background: rgba(255,255,255,.35); }
</style>
</head>
<body>
<div class="canvas">

  <!-- Letterhead, option 1 -->
  <section class="sheet letterhead" style="left:19px;top:12px;width:341px;height:463px;">
    <div class="brand" style="left:16px;top:16px;"><span class="brand-dot"></span><span class="brand-name">Varneth Systems</span></div>
    <div class="contact" style="left:200px;top:14px;">418 W. Harrow Ln.<br>Kent, WA 98047</div>
    <div class="contact" style="left:260px;top:14px;">T (253) 555-0148<br>F (253) 555-0149<br>www.varneth.example<br>dorian.kelbrook@varneth.example</div>
    <div class="faint-mark" style="left:95px;top:130px;width:150px;height:150px;"></div>
    <svg class="wave" viewBox="0 0 341 80" height="80" aria-hidden="true">
      <path d="M0 40 C90 70 220 10 341 30 L341 80 L0 80 Z" fill="var(--navy)"/>
      <path d="M0 34 C90 64 220 4 341 24" fill="none" stroke="var(--grey)" stroke-width="2"/>
      <path d="M0 28 C90 58 220 -2 341 18" fill="none" stroke="var(--grey-light)" stroke-width="1.5"/>
    </svg>
    <div class="web" style="right:20px;bottom:12px;">www.varneth.example</div>
  </section>
  <div class="option-label" style="left:176px;">Option 1</div>

  <!-- Fax sheet, option 2 -->
  <section class="sheet fax-sheet" style="left:384px;top:12px;width:336px;height:463px;">
    <div class="brand" style="left:16px;top:16px;"><span class="brand-dot"></span><span class="brand-name">Varneth Systems</span></div>
    <div class="contact" style="left:190px;top:14px;">418 W. Harrow Ln.<br>Kent, WA 98047</div>
    <div class="contact" style="left:252px;top:14px;">T (253) 555-0148<br>F (253) 555-0149<br>www.varneth.example<br>dorian.kelbrook@varneth.example</div>
    <div class="faint-mark" style="left:95px;top:140px;width:150px;height:150px;"></div>
    <h1 class="fax-title">FAX</h1>
    <div class="fax-fields">
      <div class="fax-field">To:</div><div class="fax-field">From:</div>
      <div class="fax-field">Fax:</div><div class="fax-field">Pages:</div>
      <div class="fax-field">Phone:</div><div class="fax-field">Date:</div>
      <div class="fax-field">Re:</div><div class="fax-field">CC:</div>
    </div>
    <div class="fax-checks">
      <span class="fax-check">Urgent</span><span class="fax-check">For Review</span><span class="fax-check">Please Comment</span><span class="fax-check">Please Reply</span><span class="fax-check">Please Recycle</span>
    </div>
    <svg class="wave" viewBox="0 0 336 80" height="80" aria-hidden="true">
      <path d="M0 40 C90 70 220 10 336 30 L336 80 L0 80 Z" fill="var(--navy)"/>
      <path d="M0 34 C90 64 220 4 336 24" fill="none" stroke="var(--grey)" stroke-width="2"/>
      <path d="M0 28 C90 58 220 -2 336 18" fill="none" stroke="var(--grey-light)" stroke-width="1.5"/>
    </svg>
    <div class="web" style="right:20px;bottom:12px;">www.varneth.example</div>
  </section>
  <div class="option-label" style="left:540px;">Option 2</div>

  <!-- Envelope, back with flap -->
  <section class="envelope envelope-back" style="left:734px;top:12px;width:454px;height:150px;">
    <svg class="flap" viewBox="0 0 454 150" preserveAspectRatio="none" aria-hidden="true">
      <path d="M0 0 L454 0 L454 20 L227 92 L0 20 Z" fill="var(--navy)"/>
      <path d="M0 20 L227 92 L454 20" fill="none" stroke="var(--grey)" stroke-width="2"/>
    </svg>
    <div class="flap-mark"></div>
  </section>

  <!-- Envelope, front -->
  <section class="envelope envelope-front" style="left:734px;top:150px;width:454px;height:188px;">
    <div class="brand" style="left:18px;top:30px;"><span class="brand-dot" style="width:16px;height:16px;"></span><span class="brand-name" style="font-size:13px;">Varneth Systems</span></div>
    <div class="contact" style="left:38px;top:50px;">418 W. Harrow Ln., Kent, WA 98047</div>
    <svg class="wave" viewBox="0 0 454 60" height="60" aria-hidden="true">
      <path d="M0 30 C120 60 300 5 454 22 L454 60 L0 60 Z" fill="var(--navy)"/>
      <path d="M0 24 C120 54 300 -1 454 16" fill="none" stroke="var(--grey)" stroke-width="2"/>
    </svg>
    <div class="web" style="right:18px;bottom:8px;">www.varneth.example</div>
  </section>

  <!-- Business card, front -->
  <section class="card card-front" style="left:732px;top:372px;">
    <div class="brand" style="left:10px;top:12px;"><span class="brand-dot" style="width:10px;height:10px;"></span><span class="brand-name" style="font-size:8px;">Varneth Systems</span></div>
    <div class="card-person"><strong>Dorian Kelbrook</strong><br>President &amp; Chief Architect</div>
    <div class="contact" style="left:88px;top:38px;font-size:3.8px;line-height:5px;">T (253) 555-0148<br>dorian.kelbrook@varneth.example<br>418 W. Harrow Ln.<br>Kent, WA 98047</div>
    <svg class="wave" viewBox="0 0 156 22" height="22" aria-hidden="true">
      <path d="M0 12 C40 22 100 2 156 8 L156 22 L0 22 Z" fill="var(--navy)"/>
      <path d="M0 9 C40 19 100 -1 156 5" fill="none" stroke="var(--grey)" stroke-width="1"/>
    </svg>
  </section>

  <!-- Business card, back -->
  <section class="card card-back" style="left:912px;top:372px;">
    <div class="card-back-mark"></div>
  </section>

</div>
</body>
</html>
```